Create Bourbon label for Craft Distillery located in the Foothills of NC.

Need to create a label for a craft bourbon. The brand name is Creekhollow. Looking for a traditional/vintage bottle label. I have created a concept and would like an expansion of the concept idea (open to artwork outside of concept art as well). I have included the bottle being used. Label area approx 4.25H x 3.5W. With the Creekhollow brand name, would like to incorporate trees (native to NC and Appalachia), mountains (mt pano of area included), and sawblade. However, I do not want the sawblade to be the focal point of the design. The word Bourbon, proof, abv, and 750 ml will need to be horizontal. Creekhollow and Made in NC can be angled in the design.

Requirements
Must have
• Front Label will need to contain the followingBrand Name = SawmillsBourbon750 ml100 Proof50% ABVAged 3 years

```html
<!DOCTYPE html>
<html lang="en">
<head>
<meta charset="utf-8">
<title>Creekhollow Bourbon Label</title>
<link rel="stylesheet" href="https://fonts.googleapis.com/css2?family=Rye&family=Arimo:wght@400&display=swap">
<style>
  :root {
    --backdrop: #eef1f1;
    --label-paper: #ffffff;
    --frame-brown: #6b3a14;
    --plaque-yellow: #fbe56f;
    --plaque-edge: #8a5a1c;
    --ribbon-orange: #f29a1f;
    --ribbon-shadow: #c9700f;
    --ink-brown: #5a3512;
    --ink-dark: #2b2118;
    --forest: #3f7a3a;
    --forest-light: #8fb07a;
    --mountain: #7a4a22;
  }
  html, body {
    margin: 0;
    padding: 0;
    width: 705px;
    height: 1200px;
    overflow: hidden;
    background: var(--backdrop);
  }
  .canvas {
    position: relative;
    width: 705px;
    height: 1200px;
  }
  .bourbon-label {
    position: absolute;
    left: 72px;
    top: 248px;
    width: 560px;
    height: 704px;
  }
  .brand-name {
    font-family: "Rye", serif;
    fill: var(--ink-brown);
  }
  .product-type {
    font-family: "Rye", serif;
    fill: var(--ink-brown);
  }
  .spec-text {
    font-family: "Arimo", sans-serif;
    fill: var(--ink-dark);
  }
  .ribbon-note {
    font-family: "Arimo", sans-serif;
    fill: var(--ink-brown);
  }
</style>
</head>
<body>
<main class="canvas">
  <svg class="bourbon-label" viewBox="0 0 350 440" xmlns="http://www.w3.org/2000/svg">
    <defs>
      <linearGradient id="sceneTone" x1="0" y1="0" x2="0" y2="1">
        <stop offset="0" stop-color="#a07a58" stop-opacity="0.5"/>
        <stop offset="0.3" stop-color="var(--forest-light)"/>
        <stop offset="0.7" stop-color="var(--forest)"/>
        <stop offset="1" stop-color="#6b4320"/>
      </linearGradient>
    </defs>

    <rect class="label-paper" x="2" y="2" width="346" height="436" fill="var(--label-paper)" stroke="var(--frame-brown)" stroke-width="4"/>

    <rect class="scene-illustration" role="img" aria-label="Brown mountain peaks above a forest of Appalachian evergreen pines, with a brown saw blade beneath the ribbon" x="12" y="36" width="326" height="382" rx="40" fill="url(#sceneTone)" opacity="0.85"/>

    <path class="brand-plaque" d="M46 172 H304 Q302 182 312 186 V304 Q302 308 304 318 H46 Q48 308 38 304 V186 Q48 182 46 172 Z" fill="var(--plaque-yellow)" stroke="var(--plaque-edge)" stroke-width="2.5"/>
    <rect class="plaque-inner" x="56" y="182" width="238" height="100" fill="none" stroke="var(--plaque-edge)" stroke-width="1"/>

    <text class="brand-name" x="175" y="256" text-anchor="middle" font-size="28" textLength="220" lengthAdjust="spacingAndGlyphs">CREEKHOLLOW</text>
    <text class="spec-text" x="175" y="299" text-anchor="middle" font-size="12">750 ML</text>
    <text class="spec-text" x="100" y="312" text-anchor="middle" font-size="7.5">100 Proof</text>
    <text class="spec-text" x="250" y="312" text-anchor="middle" font-size="7.5">50%ABV</text>

    <path class="ribbon-tail" d="M8 352 L48 338 L56 370 L26 382 L34 366 Z" fill="var(--ribbon-orange)" stroke="var(--ribbon-shadow)" stroke-width="1"/>
    <path class="ribbon-tail" d="M342 352 L302 338 L294 370 L324 382 L316 366 Z" fill="var(--ribbon-orange)" stroke="var(--ribbon-shadow)" stroke-width="1"/>
    <path class="ribbon-band" d="M46 332 Q175 318 304 332 L300 368 Q175 354 50 368 Z" fill="var(--ribbon-orange)" stroke="var(--ribbon-shadow)" stroke-width="1.5"/>
    <path class="ribbon-inner" d="M58 336 Q175 324 292 336 L289 362 Q175 350 61 362 Z" fill="none" stroke="var(--frame-brown)" stroke-width="1.2"/>

    <text class="product-type" x="175" y="358" text-anchor="middle" font-size="22">BOURBON</text>
    <text class="ribbon-note" x="34" y="364" text-anchor="middle" font-size="6">Aged</text>
    <text class="ribbon-note" x="316" y="364" text-anchor="middle" font-size="6">3 Years</text>
  </svg>
</main>
</body>
</html>
```